Preferred pricing vendor

We are a plumbing company that has many services
-Boilers & Controls
-Plumbing & Heating
-HVAC & Refrigeration
-Preventative Maintenacne
-Gas fitting & Drain Cleaning

We primarily look after condo buildings, and our preferred service rates ($98, $93, or $88 depending on the contract) extend to all of our clients. So in essence, we look after the mechanical room and common equipment but our clients can call us in for drain cleaning or replacing a fixture in their suite. The discounted rates apply to the personal residence. We want a flyer to let them know they get a discount on our services. A one-pager we can send out to all of our contract clients.

Included source files for our letterhead and logo just so you can see the colours we go with.

Target Market(s)

Residential repairs, individual people, replacement of fixtures in-suite specific repairs

Requirements
Must have
• be colourful and attractive

```html
<!DOCTYPE html>
<html lang="en">
<head>
<meta charset="utf-8">
<title>Keystone Mechanical Inc – Preferred Rates Flyer</title>
<link rel="stylesheet" href="https://fonts.googleapis.com/css2?family=Roboto+Condensed:wght@400;500;700&family=Roboto:wght@400;500;700&display=swap">
<style>
  :root {
    --navy: #16294a;
    --navy-deep: #0f1f3a;
    --orange: #f15a24;
    --blue: #1f6fc9;
    --blue-light: #2d86e0;
    --ink: #3a3d4a;
    --white: #ffffff;
    --page: #e9eaee;
  }
  * { box-sizing: border-box; margin: 0; padding: 0; }
  html, body { width: 1200px; height: 819px; overflow: hidden; background: var(--page); }
  .flyer {
    position: absolute; left: 293px; top: 13px;
    width: 613px; height: 792px; background: var(--white);
    overflow: hidden; font-family: "Roboto Condensed", sans-serif;
    box-shadow: 0 4px 14px rgba(0,0,0,.18);
  }
  .hero { position: absolute; left: 0; top: 0; width: 613px; height: 328px; background: var(--navy); }
  .brand { position: absolute; left: 38px; top: 40px; width: 230px; text-align: center; }
  .brand-dot { width: 62px; height: 62px; border-radius: 50%; background: var(--orange); margin: 0 auto 12px; }
  .brand-name { color: var(--white); font-weight: 700; font-size: 30px; letter-spacing: 1px; line-height: 1; }
  .brand-sub { color: var(--white); font-weight: 700; font-size: 14px; letter-spacing: 2px; margin-top: 6px; }
  .headline { position: absolute; left: 37px; top: 198px; font-weight: 700; font-size: 29px; line-height: 34px; color: var(--white); }
  .headline .accent { color: var(--orange); }
  .gear-art { position: absolute; left: 0; top: 0; }
  .package {
    position: absolute; left: 356px; top: 302px; width: 247px; height: 412px;
    background: linear-gradient(180deg, var(--blue-light), var(--blue));
    border-radius: 0 0 18px 18px;
  }
  .package-title { position: absolute; left: 16px; top: 72px; color: var(--white); font-family: Roboto, sans-serif; font-weight: 700; font-size: 14px; line-height: 22px; }
  .price-pill {
    position: absolute; left: 15px; top: 152px; width: 215px; height: 32px; border-radius: 16px;
    background: var(--orange); color: var(--white); font-family: Roboto, sans-serif; font-weight: 700; font-size: 14.5px;
    display: flex; align-items: center; justify-content: center;
  }
  .discount { position: absolute; left: 0; top: 196px; width: 242px; text-align: center; color: var(--white); font-family: Roboto, sans-serif; font-size: 12px; }
  .mission { position: absolute; left: 23px; top: 234px; width: 209px; color: var(--white); font-family: Roboto, sans-serif; font-size: 12px; line-height: 14.5px; text-align: justify; }
  .services-bar {
    position: absolute; left: 0; top: 341px; width: 316px; height: 35px; background: var(--orange);
    border-radius: 0 18px 18px 0; color: var(--white); font-weight: 700; font-size: 22px;
    padding-left: 42px; line-height: 40px;
  }
  .service-list { position: absolute; left: 40px; top: 396px; list-style: none; }
  .service { display: flex; align-items: center; height: 54px; }
  .service svg { width: 48px; height: 48px; flex: none; }
  .service span { margin-left: 13px; color: var(--ink); font-weight: 500; font-size: 16.5px; }
  .footer { position: absolute; left: 0; top: 739px; width: 613px; height: 53px; background: var(--navy); }
  .estimate {
    position: absolute; left: 46px; top: 731px; width: 210px; height: 38px; background: var(--orange);
    clip-path: polygon(0 0, 100% 0, 96% 100%, 4% 100%);
    color: var(--white); font-weight: 700; font-size: 16px; display: flex; align-items: center; justify-content: center;
  }
  .contact { position: absolute; top: 757px; display: flex; align-items: center; gap: 6px; color: var(--white); font-family: Roboto, sans-serif; font-weight: 700; font-size: 14px; }
  .contact svg { width: 17px; height: 17px; }
</style>
</head>
<body>
<main class="flyer">
  <section class="hero">
    <div class="brand">
      <div class="brand-dot"></div>
      <div class="brand-name">KEYSTONE</div>
      <div class="brand-sub">MECHANICAL INC</div>
    </div>
    <h1 class="headline">AFFORDABLE<br><span class="accent">MECHANICAL SYSTEM</span><br>MAINTENANCE</h1>
  </section>

  <div class="package">
    <p class="package-title">CHOOSE YOUR<br>MAINTENANCE PACKAGE<br>OR CUSTOMIZE YOUR OWN</p>
    <div class="price-pill">PRICES FROM $88 - $98</div>
    <p class="discount">DISCOUNT ON OUR SERVICES</p>
    <p class="mission">Our goal in creating a partnership with owners and boards is to advise on the best path to maintain and service building equipment in order to protect assets and investments, long term. Our mandate is to provide our services with honesty, integrity, and offer more communication as the building blocks of trust.</p>
  </div>

  <svg class="gear-art" width="613" height="360" viewBox="0 0 613 360">
    <defs>
      <linearGradient id="photoTone" x1="0" y1="0" x2="1" y2="1">
        <stop offset="0" stop-color="#c9ccd2"/>
        <stop offset=".55" stop-color="#4a505c"/>
        <stop offset="1" stop-color="#1e2533"/>
      </linearGradient>
    </defs>
    <g fill="var(--orange)">
      <circle cx="471" cy="157" r="166"/>
      <rect x="446" y="-22" width="50" height="30" rx="4"/>
      <rect x="446" y="306" width="50" height="38" rx="4"/>
      <rect x="282" y="132" width="30" height="50" rx="4"/>
      <rect x="312" y="40" width="34" height="46" rx="4" transform="rotate(-45 329 63)"/>
      <rect x="312" y="228" width="34" height="46" rx="4" transform="rotate(45 329 251)"/>
      <rect x="578" y="235" width="36" height="46" rx="4" transform="rotate(-45 596 258)"/>
    </g>
    <circle cx="471" cy="157" r="145" fill="url(#photoTone)" stroke="var(--white)" stroke-width="3" role="img" aria-label="Photo of a technician in a hard hat servicing a boiler pump"/>
  </svg>

  <div class="services-bar">OUR SERVICES</div>
  <ul class="service-list">
    <li class="service"><svg viewBox="0 0 48 48"><circle cx="24" cy="24" r="22" fill="var(--orange)"/><circle cx="24" cy="24" r="17" fill="var(--blue)"/><rect x="19" y="14" width="10" height="20" rx="3" fill="#fff"/></svg><span>BOILERS &amp; CONTROLS</span></li>
    <li class="service"><svg viewBox="0 0 48 48"><circle cx="24" cy="24" r="22" fill="var(--orange)"/><circle cx="24" cy="24" r="17" fill="var(--blue)"/><path d="M15 19h14v5h4v6h-5v-3H15z" fill="#fff"/><circle cx="31" cy="34" r="1.8" fill="#fff"/></svg><span>PLUMBING &amp; HEATING</span></li>
    <li class="service"><svg viewBox="0 0 48 48"><circle cx="24" cy="24" r="22" fill="var(--orange)"/><circle cx="24" cy="24" r="17" fill="var(--blue)"/><circle cx="24" cy="24" r="9" fill="none" stroke="#fff" stroke-width="2"/><path d="M24 24l0-8M24 24l7 4M24 24l-7 4" stroke="#fff" stroke-width="3"/></svg><span>HVAC &amp; REFRIGERATION</span></li>
    <li class="service"><svg viewBox="0 0 48 48"><circle cx="24" cy="24" r="22" fill="var(--orange)"/><circle cx="24" cy="24" r="17" fill="var(--blue)"/><path d="M16 33l10-10M28 15a5 5 0 0 0-4 7l6 6a5 5 0 0 0 7-4l-3 1-3-3 1-3z" stroke="#fff" stroke-width="3" fill="none" stroke-linecap="round"/></svg><span>PREVENTATIVE MAINTENACNE</span></li>
    <li class="service"><svg viewBox="0 0 48 48"><circle cx="24" cy="24" r="22" fill="var(--orange)"/><circle cx="24" cy="24" r="17" fill="var(--blue)"/><path d="M24 13c2 5 7 8 7 13a7 7 0 0 1-14 0c0-4 3-5 4-9 1 3 3 3 3-4z" fill="#fff"/></svg><span>GAS FITTING &amp; DRAIN CLEANING</span></li>
    <li class="service"><svg viewBox="0 0 48 48"><circle cx="24" cy="24" r="22" fill="var(--orange)"/><circle cx="24" cy="24" r="17" fill="var(--blue)"/><path d="M26 13l-9 13h7l-2 9 9-13h-7z" fill="#fff"/></svg><span>ELECTRICAL SERVICES</span></li>
  </ul>

  <footer class="footer"></footer>
  <div class="estimate">FREE ESTIMATE!</div>
  <div class="contact" style="left:268px">
    <svg viewBox="0 0 18 18"><circle cx="9" cy="9" r="8" fill="none" stroke="var(--orange)" stroke-width="1.5"/><path d="M6 5l2 0 1 2-1.2 1a5 5 0 0 0 2.2 2.2L11 9l2 1v2a1 1 0 0 1-1 1A7 7 0 0 1 5 6a1 1 0 0 1 1-1z" fill="var(--orange)"/></svg>
    (403) 555-0187
  </div>
  <div class="contact" style="left:419px">
    <svg viewBox="0 0 18 18"><g fill="none" stroke="var(--orange)" stroke-width="1.4"><circle cx="9" cy="9" r="8"/><ellipse cx="9" cy="9" rx="3.5" ry="8"/><path d="M1 9h16M2.5 5h13M2.5 13h13"/></g></svg>
    keystonemechanical.ca
  </div>
</main>
</body>
</html>
```